KWT BUSINESS CARD

I'd like a new business card for the folks in my office. I recently became aware of a company that produces extra thick cards that seem to me to make excellent use of embossing. I have a logo that I like so I just need a design that uses embossing effectively, is simple and uses minimal color.

I am uploading our current logo of a tooth with a brush above it. I am also uploading another file with the words of our business. In your design please use the square version of the tooth vs. the strectched version. The original logo is the more square image but please use the words and the fonts of "Wexmoor Dental Group" and incorporate that in the design.

Industry/Entity Type

Business

Colors
ffffff

Requirements
Must have
• Logo, company name (also a part of our existing logo), employee name and title, phone number and website address. Must be simple
Nice to have
• Embossed - Maybe a solid color on the back
Should not have
• Must not be too complex or busy

```html
<!DOCTYPE html>
<html lang="en">
<head>
<meta charset="utf-8">
<title>Wexmoor Dental Group – Business Card</title>
<link href="https://fonts.googleapis.com/css2?family=Arimo:wght@400;700&display=swap" rel="stylesheet">
<style>
  :root {
    --brand-blue: #2a2a84;
    --brand-green: #138a36;
    --ink: #1d1d1d;
    --muted: #4a4a4a;
    --paper: #ffffff;
    --backdrop: #d9d9db;
  }
  * { box-sizing: border-box; margin: 0; padding: 0; }
  html, body {
    width: 1200px; height: 675px; overflow: hidden;
    background: var(--backdrop);
    font-family: "Arimo", Arial, sans-serif;
  }
  .stage { position: relative; width: 1200px; height: 675px; }

  .card {
    position: absolute; top: 58px;
    width: 320px; height: 560px;
    box-shadow: 0 4px 14px rgba(0,0,0,.18);
    overflow: hidden;
  }

  /* Front */
  .card--front { left: 250px; background: var(--paper); }
  .edge-band {
    position: absolute; left: 0; top: 0; width: 24px; height: 100%;
    background: linear-gradient(to bottom, var(--brand-blue) 0 74%, var(--brand-green) 74% 100%);
  }
  .wordmark {
    position: absolute; left: 62px; top: 150px;
    display: flex; align-items: center; gap: 12px;
  }
  .wordmark__square {
    width: 58px; height: 58px; background: var(--brand-blue);
  }
  .wordmark__name {
    color: var(--ink); font-weight: 700; text-transform: uppercase;
    font-size: 15px; line-height: 1.15; letter-spacing: .06em;
  }
  .contact { position: absolute; left: 62px; top: 380px; }
  .contact__name {
    color: var(--brand-green); font-weight: 700; font-size: 19px;
  }
  .contact__title { color: var(--muted); font-size: 13px; margin-top: 4px; }
  .contact__list { list-style: none; margin-top: 22px; }
  .contact__list li {
    display: flex; align-items: center; gap: 9px;
    color: var(--ink); font-size: 14px; line-height: 19px;
  }
  .contact__list svg { width: 13px; height: 13px; fill: var(--brand-green); }
  .contact__web {
    color: var(--brand-green); font-weight: 700; font-size: 13px; margin-top: 12px;
  }

  /* Back */
  .card--back { left: 630px; background: var(--brand-blue); }
  .back-wordmark {
    position: absolute; left: 200px; top: 480px;
    transform: rotate(-90deg); transform-origin: left top;
    display: flex; align-items: center; gap: 12px;
    color: var(--paper); font-weight: 700; text-transform: uppercase;
    font-size: 17px; letter-spacing: .06em; white-space: nowrap;
  }
  .back-wordmark__square { width: 34px; height: 34px; background: var(--paper); }
</style>
</head>
<body>
<main class="stage">
  <section class="card card--front" aria-label="Card front">
    <div class="edge-band"></div>
    <div class="wordmark">
      <span class="wordmark__square"></span>
      <span class="wordmark__name">Wexmoor<br>Dental<br>Group</span>
    </div>
    <div class="contact">
      <p class="contact__name">Marcel Dorne</p>
      <p class="contact__title">Principal</p>
      <ul class="contact__list">
        <li><svg viewBox="0 0 16 16" aria-hidden="true"><path d="M3 1h3l1.5 4-2 1.3a9 9 0 0 0 4.2 4.2L11 8.5l4 1.5v3a2 2 0 0 1-2 2A13 13 0 0 1 1 3a2 2 0 0 1 2-2z"/></svg>555.201.4470</li>
        <li><svg viewBox="0 0 16 16" aria-hidden="true"><path d="M4 1h8v4H4zM1 6h14v7h-3v2H4v-2H1zm4 5v3h6v-3z"/></svg>555.201.4471</li>
        <li><svg viewBox="0 0 16 16" aria-hidden="true"><path d="M1 3h14v10H1zm1.5 1.2V5l5.5 4 5.5-4v-.8z"/></svg>md@wexmoordental.com</li>
      </ul>
      <p class="contact__web">www.wexmoordental.com</p>
    </div>
  </section>

  <section class="card card--back" aria-label="Card back">
    <div class="back-wordmark">
      <span class="back-wordmark__square"></span>
      <span>Wexmoor Dental Group</span>
    </div>
  </section>
</main>
</body>
</html>
```